vantoreq realty business card

We need a Business card for our new business. The logo was designed by BrushQuill, and the text We want on the back is:
REAL ESTATE INVESTMENTS
- BUY, RENOVATE, SELL AND RENT RESIDENTIAL PROPERTIES
- FULL HOME REHABBING , REMODELING AND INTERIOR DESIGN
- HOME STAGING SERVICES
- WHOLESALE INVESTOR PROPERTIES
- MAKE CASH OFFERS ON HOUSES IN ANY CONDITION AND IN ANY SITUATION
- PRIVATE MONEY INVESTOR PROGRAMS WITH 6-12% RETURNS
- PAY CASH REWARDS FOR REFFERALS
- CONCIERGE SERVICE

Business

```html
<!DOCTYPE html>
<html lang="en">
<head>
<meta charset="utf-8">
<title>vantoreq Realty – Business Card</title>
<link href="https://fonts.googleapis.com/css2?family=Open+Sans:wght@300;400;600&display=swap" rel="stylesheet">
<style>
  :root {
    --page-bg: #e9e7e3;
    --card-white: #f7f7f7;
    --teal-light: #bfe7ea;
    --teal: #9fd6db;
    --teal-deep: #8ccbd1;
    --band-grey: #a8a9ab;
    --brand-teal: #7cc3cb;
    --text-grey: #8d8e90;
    --white: #ffffff;
  }
  * { box-sizing: border-box; margin: 0; padding: 0; }
  html, body { width: 1200px; height: 1000px; overflow: hidden; }
  body {
    background: var(--page-bg);
    font-family: "Open Sans", Arial, sans-serif;
    position: relative;
  }
  .card {
    position: absolute;
    left: 240px;
    width: 720px;
    height: 411px;
    background: var(--card-white);
    box-shadow: 0 6px 18px rgba(0,0,0,0.18);
    overflow: hidden;
  }
  .card--front { top: 60px; }
  .card--back { top: 530px; }

  .teal-field {
    position: absolute;
    left: 0; right: 0;
    background: linear-gradient(120deg, var(--teal-deep) 0%, var(--teal) 45%, var(--teal-light) 100%);
  }
  .card--front .teal-field { top: 0; height: 250px; }
  .card--back .teal-field { top: 170px; bottom: 0; }

  .position {
    position: absolute;
    top: 34px; right: 40px;
    color: var(--white);
    font-size: 17px;
    font-weight: 300;
    line-height: 22px;
  }
  .name-band {
    position: absolute;
    top: 66px; left: 300px; right: 0;
    height: 56px;
    background: var(--band-grey);
    display: flex; align-items: center;
    padding-left: 26px;
  }
  .person-name {
    color: var(--white);
    font-size: 38px;
    font-weight: 400;
    line-height: 1;
    letter-spacing: 0.5px;
  }
  .contact-list {
    position: absolute;
    top: 146px; left: 420px;
    list-style: none;
    color: var(--white);
    font-size: 16px;
    font-weight: 400;
    letter-spacing: 0.5px;
  }
  .contact-list li { display: flex; align-items: center; gap: 10px; height: 30px; }
  .contact-list svg { width: 13px; height: 13px; flex: none; }

  .brand {
    position: absolute;
    display: flex; flex-direction: column;
  }
  .card--front .brand { left: 90px; top: 300px; }
  .card--back .brand { left: 90px; top: 56px; }
  .brand-line { display: flex; align-items: center; gap: 12px; }
  .brand-mark { width: 22px; height: 22px; background: var(--band-grey); }
  .brand-name {
    color: var(--brand-teal);
    font-size: 34px;
    font-weight: 400;
    letter-spacing: 0.5px;
  }
  .brand-tagline {
    margin-top: 4px;
    margin-left: 34px;
    color: var(--text-grey);
    font-size: 14px;
    font-weight: 400;
    letter-spacing: 1.6px;
  }

  .section-band {
    position: absolute;
    top: 194px; left: 300px; right: 0;
    height: 40px;
    background: var(--band-grey);
    display: flex; align-items: center;
    padding-left: 22px;
  }
  .section-band h2 {
    color: var(--white);
    font-size: 22px;
    font-weight: 600;
    letter-spacing: 1px;
  }
  .service-list {
    position: absolute;
    top: 246px; left: 300px; right: 30px;
    list-style: none;
    color: var(--white);
    font-size: 14px;
    font-weight: 400;
    line-height: 17px;
  }
  .service-list li { position: relative; padding-left: 16px; }
  .service-list li::before {
    content: "";
    position: absolute; left: 0; top: 5px;
    width: 7px; height: 7px;
    background: var(--white);
  }
</style>
</head>
<body>

<section class="card card--front" aria-label="Business card front">
  <div class="teal-field"></div>
  <p class="position">your position</p>
  <div class="name-band"><span class="person-name">John Doe</span></div>
  <ul class="contact-list">
    <li>
      <svg viewBox="0 0 13 13"><rect x="0.5" y="2.5" width="12" height="8" fill="#fff"/><path d="M0.5 2.5 L6.5 7 L12.5 2.5" stroke="#9fd6db" fill="none"/></svg>
      yourname@vantoreq.com
    </li>
    <li>
      <svg viewBox="0 0 13 13"><rect x="3" y="0.5" width="7" height="12" rx="1" fill="none" stroke="#fff" stroke-width="1.3"/></svg>
      123.456.7890
    </li>
    <li>
      <svg viewBox="0 0 13 13"><circle cx="6.5" cy="6.5" r="6" fill="#fff"/><path d="M0.5 6.5 H12.5 M6.5 0.5 V12.5" stroke="#9fd6db"/></svg>
      www.vantoreq.com
    </li>
  </ul>
  <div class="brand">
    <div class="brand-line"><span class="brand-mark"></span><span class="brand-name">VANTOREQRealty</span></div>
    <span class="brand-tagline">REAL ESTATE SOLUTIONS</span>
  </div>
</section>

<section class="card card--back" aria-label="Business card back">
  <div class="teal-field"></div>
  <div class="brand">
    <div class="brand-line"><span class="brand-mark"></span><span class="brand-name">VANTOREQRealty</span></div>
    <span class="brand-tagline">REAL ESTATE SOLUTIONS</span>
  </div>
  <div class="section-band"><h2>REAL ESTATE INVESTMENTS</h2></div>
  <ul class="service-list">
    <li>Buy, renovate, sell and rent residential properties</li>
    <li>Full home rehabbing , remodeling and interior design</li>
    <li>Home staging services</li>
    <li>Wholesale investor properties</li>
    <li>Make cash offers on houses in any condition and in any situation</li>
    <li>Private money investor programs with 6-12% returns</li>
    <li>Pay cash rewards for refferals</li>
    <li>Concierge service</li>
  </ul>
</section>

</body>
</html>
```